A5 Flyer & A3 poster design for Velvet Lobes

Velvet Lobes are a fun new accesories brand based in the UK

Create an A5 Flyer , A4 poster and simple website under construction landing page.

1. A5 Flyer - Portrait

- Hand drawn example attached showing rough layout. To include 6 pictures (attached) in polaroid format hung on a line using pegs.
- Pictures to be cropped to fit in 6 same size boxes.
- Logo attached
- NEW to be written in the same pink as logo.
- Create a background in keeping with the style of the logo and images

2. A4 poster - Portrait

- The same style , colour and font as the Flyer.
- The same six images just bigger.
- Example layout attached.

COPY FOR FLYER

Brand New Quality Clip-on ears
Soft & light weight for comfortable wear
Perfect for parties, festivals & nights out
Available in a variety of quality faux fur colours with sparkle or velour centre
Great for adults or kids

Email: hello@velvetlobes.co.uk
Call: 07913 284 571
Web: www.velvetlobes.co.uk

Target Market(s)

Females 18 - 40

Industry/Entity Type

Construction

Requirements
Must have
• must be modern. no dated flyer backgrounds

```html
<!DOCTYPE html>
<html lang="en">
<head>
<meta charset="utf-8">
<title>Velvet Lobes – Flyer &amp; Poster</title>
<link rel="stylesheet" href="https://fonts.googleapis.com/css2?family=Baloo+2:wght@400;600;700;800&display=swap">
<style>
  :root {
    --pink: #e6197f;
    --pink-light: #f39ac4;
    --yellow: #ffd400;
    --orange: #f7941d;
    --blue: #4cb8e6;
    --blue-deep: #1a75bb;
    --peg: #f3d88e;
    --rope: #b8932e;
    --white: #ffffff;
  }
  html, body {
    margin: 0;
    width: 1200px;
    height: 1200px;
    overflow: hidden;
    background: var(--white);
    font-family: "Baloo 2", sans-serif;
  }
  .canvas { position: relative; width: 1200px; height: 1200px; }
  .flyer-a5 { position: absolute; left: 0; top: 0; width: 330px; height: 466px; }
  .poster-a3 { position: absolute; left: 352px; top: 0; width: 848px; height: 1200px; }
  .brand-name { font-family: "Baloo 2", sans-serif; font-weight: 800; fill: var(--pink); }
  .badge-text { font-family: "Baloo 2", sans-serif; font-weight: 800; fill: var(--pink); }
  .feature { font-family: "Baloo 2", sans-serif; font-weight: 700; font-style: italic; fill: var(--white); font-size: 29px; }
  .contact-label { font-family: "Baloo 2", sans-serif; font-weight: 400; fill: var(--pink-light); font-size: 30px; }
  .contact-value { font-family: "Baloo 2", sans-serif; font-weight: 700; font-style: italic; fill: var(--white); font-size: 30px; }
  .tagline { font-family: "Baloo 2", sans-serif; font-weight: 800; fill: var(--white); font-size: 46px; }
</style>
</head>
<body>
<div class="canvas">
  <svg width="0" height="0" style="position:absolute">
    <defs>
      <linearGradient id="photoTone" x1="0" y1="0" x2="1" y2="1">
        <stop offset="0" stop-color="#c9a48e"/>
        <stop offset="0.5" stop-color="#8a6a5c"/>
        <stop offset="1" stop-color="#3e3432"/>
      </linearGradient>
      <linearGradient id="darkEarsTone" x1="0" y1="0" x2="1" y2="0">
        <stop offset="0" stop-color="#f4eeee"/>
        <stop offset="0.5" stop-color="#6b1a22"/>
        <stop offset="1" stop-color="#f4eeee"/>
      </linearGradient>
      <linearGradient id="lightEarsTone" x1="0" y1="0" x2="1" y2="0">
        <stop offset="0" stop-color="#ffffff"/>
        <stop offset="0.5" stop-color="#d2b49e"/>
        <stop offset="1" stop-color="#ffffff"/>
      </linearGradient>

      <symbol id="velvet-lobes-layout" viewBox="0 0 1060 1500">
        <!-- background bands -->
        <rect class="band-yellow" x="0" y="0" width="1060" height="800" fill="var(--yellow)"/>
        <path class="band-orange" d="M0,470 C260,420 520,330 1060,250 V780 H0Z" fill="var(--orange)"/>
        <path class="band-pink-light" d="M0,80 C400,120 850,110 1060,40 V120 C850,170 400,170 0,150Z" fill="var(--pink-light)"/>
        <path class="band-pink" d="M0,0 H1060 V40 C850,110 400,120 0,80Z" fill="var(--pink)"/>
        <path class="band-blue" d="M0,740 C380,790 700,770 1060,730 V1500 H0Z" fill="var(--blue)"/>
        <path class="band-blue-deep" d="M0,1280 C320,1320 700,1300 1060,1220 V1500 H0Z" fill="var(--blue-deep)"/>

        <!-- brand name -->
        <text class="brand-name" x="90" y="300" font-size="150">Velvet</text>
        <text class="brand-name" x="120" y="440" font-size="150">Lobes</text>

        <!-- NEW badge -->
        <circle cx="830" cy="150" r="108" fill="var(--pink)"/>
        <circle cx="830" cy="150" r="98" fill="#fbe0ee"/>
        <text class="badge-text" x="830" y="180" font-size="92" text-anchor="middle">NEW</text>

        <!-- product shots -->
        <g class="product-card" transform="rotate(-2 820 390)">
          <rect x="640" y="265" width="360" height="245" fill="var(--yellow)"/>
          <rect x="655" y="275" width="330" height="220" fill="url(#darkEarsTone)" role="img" aria-label="Photo of black faux fur clip-on ears with red velour centre"/>
        </g>
        <g class="product-card">
          <rect x="692" y="490" width="368" height="238" fill="var(--yellow)"/>
          <rect x="710" y="505" width="316" height="205" fill="url(#lightEarsTone)" role="img" aria-label="Photo of beige faux fur clip-on ears with sparkle centre"/>
        </g>

        <!-- feature list -->
        <g class="features" fill="var(--white)">
          <circle cx="52" cy="510" r="8"/><circle cx="70" cy="510" r="8"/>
          <circle cx="52" cy="546" r="8"/><circle cx="70" cy="546" r="8"/>
          <circle cx="52" cy="582" r="8"/><circle cx="70" cy="582" r="8"/>
          <circle cx="52" cy="618" r="8"/><circle cx="70" cy="618" r="8"/>
          <circle cx="52" cy="691" r="8"/><circle cx="70" cy="691" r="8"/>
        </g>
        <text class="feature" x="98" y="520">Brand New Quality Clip-on ears</text>
        <text class="feature" x="98" y="556">Soft &amp; light weight for comfortable wear</text>
        <text class="feature" x="98" y="592">Perfect for parties, festivals &amp; nights out</text>
        <text class="feature" x="98" y="628">Available in a variety of quality</text>
        <text class="feature" x="98" y="665">faux fur colours with sparkle or velour centre</text>
        <text class="feature" x="98" y="701">Great for adults or kids</text>

        <!-- ropes -->
        <path class="rope" d="M0,745 C300,790 700,800 1060,735" fill="none" stroke="var(--rope)" stroke-width="6"/>
        <path class="rope" d="M0,1030 C300,1080 700,1085 1060,1015" fill="none" stroke="var(--rope)" stroke-width="6"/>

        <!-- hanging photos -->
        <g class="hung-photo" transform="translate(250 905) rotate(8)">
          <polygon points="-92,-130 92,-130 92,130 0,105 -92,130" fill="var(--pink)"/>
          <rect x="-74" y="-112" width="148" height="200" fill="url(#photoTone)" role="img" aria-label="Photo of a woman wearing fluffy party ears"/>
          <rect x="-7" y="-155" width="14" height="45" fill="var(--peg)"/>
        </g>
        <g class="hung-photo" transform="translate(530 925)">
          <polygon points="-82,-125 82,-125 82,135 0,110 -82,135" fill="var(--pink)"/>
          <rect x="-66" y="-88" width="132" height="190" fill="url(#photoTone)" role="img" aria-label="Photo of a woman wearing pink party ears"/>
          <rect x="-7" y="-175" width="14" height="45" fill="var(--peg)"/>
        </g>
        <g class="hung-photo" transform="translate(820 890) rotate(-8)">
          <polygon points="-90,-130 90,-130 90,135 0,110 -90,135" fill="var(--pink)"/>
          <rect x="-72" y="-112" width="144" height="200" fill="url(#photoTone)" role="img" aria-label="Photo of a woman wearing beige party ears"/>
          <rect x="-7" y="-160" width="14" height="45" fill="var(--peg)"/>
        </g>
        <g class="hung-photo" transform="translate(230 1205) rotate(4)">
          <polygon points="-82,-120 82,-120 82,130 0,108 -82,130" fill="var(--pink)"/>
          <rect x="-66" y="-100" width="132" height="195" fill="url(#photoTone)" role="img" aria-label="Photo of two friends wearing party ears"/>
          <rect x="-7" y="-190" width="14" height="45" fill="var(--peg)"/>
        </g>
        <g class="hung-photo" transform="translate(520 1205) rotate(-4)">
          <polygon points="-84,-125 84,-125 84,135 0,110 -84,135" fill="var(--pink)"/>
          <rect x="-68" y="-105" width="136" height="205" fill="url(#photoTone)" role="img" aria-label="Photo of a group of friends wearing party ears"/>
          <rect x="-7" y="-150" width="14" height="45" fill="var(--peg)"/>
        </g>
        <g class="hung-photo" transform="translate(840 1160) rotate(-6)">
          <polygon points="-90,-125 90,-125 90,130 0,108 -90,130" fill="var(--pink)"/>
          <rect x="-74" y="-105" width="148" height="195" fill="url(#photoTone)" role="img" aria-label="Photo of two women at a party wearing ears"/>
          <rect x="-7" y="-155" width="14" height="45" fill="var(--peg)"/>
        </g>

        <!-- footer contact -->
        <rect class="footer" x="0" y="1340" width="612" height="160" fill="var(--pink)"/>
        <text class="contact-label" x="98" y="1380">Email</text>
        <text class="contact-label" x="98" y="1416">Call</text>
        <text class="contact-label" x="98" y="1452">Web</text>
        <text class="contact-label" x="180" y="1380">:</text>
        <text class="contact-label" x="180" y="1416">:</text>
        <text class="contact-label" x="180" y="1452">:</text>
        <text class="contact-value" x="196" y="1380">hello@velvetlobes.co.uk</text>
        <text class="contact-value" x="196" y="1416">07913 284 571</text>
        <text class="contact-value" x="196" y="1452">www.velvetlobes.co.uk</text>

        <!-- tagline banners -->
        <rect x="975" y="1260" width="85" height="70" fill="var(--yellow)"/>
        <rect x="975" y="1330" width="85" height="75" fill="var(--orange)"/>
        <polygon points="636,1340 975,1255 975,1345 636,1420" fill="var(--pink)"/>
        <polygon points="636,1430 975,1355 975,1445 636,1500" fill="var(--pink)"/>
        <text class="tagline" x="720" y="1385" transform="rotate(-13 720 1385)">Playfull</text>
        <text class="tagline" x="730" y="1465" transform="rotate(-13 730 1465)">Fun</text>
      </symbol>
    </defs>
  </svg>

  <svg class="flyer-a5" viewBox="0 0 1060 1500" role="group" aria-label="Velvet Lobes A5 flyer">
    <use href="#velvet-lobes-layout" width="1060" height="1500"/>
  </svg>

  <svg class="poster-a3" viewBox="0 0 1060 1500" role="group" aria-label="Velvet Lobes poster">
    <use href="#velvet-lobes-layout" width="1060" height="1500"/>
  </svg>
</div>
</body>
</html>
```